Urgent Care Postcard Launch

We are launching a pediatric only urgent care. The postcard will be hand-delivered to local medical providers and business owners.

Reason: I was traveling with spotty internet and was unable to provide feedback. Thanks for your understanding!

All designs need to have a focus on Urgent Care. Where the lines say "opening soon" it needs to be specific to Urgent Care as a we are already open for primary care. Thanks.

Target Market(s)

Parents/grandparents of children 0-17 years old.

Industry/Entity Type

Medical

Requirements
Must have
• Opening date of September 1, 2014
Hours of operation - weekdays 5pm-9pm/weekends and holidays 9am-5pm
Phone #(405)628-3194
website - www.tinyoakclinic.com
Logo
List of things we can treat (see previous flyers)

```html
<!DOCTYPE html>
<html lang="en">
<head>
<meta charset="utf-8">
<title>Tiny Oak Pediatrics – Urgent Care Postcard</title>
<link href="https://fonts.googleapis.com/css2?family=Cabin:wght@400;500;600;700&display=swap" rel="stylesheet">
<style>
  :root {
    --red: #f0212c;
    --blue: #1fa9dd;
    --brand: #8a6a3a;
    --ink: #222;
    --paper: #ffffff;
    --backdrop: #ecebe8;
  }
  * { margin: 0; padding: 0; box-sizing: border-box; }
  html, body { width: 827px; height: 1200px; overflow: hidden; }
  body {
    background: var(--backdrop);
    font-family: "Cabin", Arial, sans-serif;
    position: relative;
  }
  .card {
    position: absolute;
    left: 66px;
    width: 691px;
    height: 534px;
    background: var(--paper);
    overflow: hidden;
    box-shadow: 0 2px 6px rgba(0,0,0,.18);
  }
  .card--front { top: 58px; }
  .card--back { top: 605px; }

  .brand {
    position: absolute;
    display: flex;
    align-items: center;
    gap: 10px;
    color: var(--brand);
    font-weight: 700;
    line-height: 1.05;
    z-index: 2;
  }
  .brand__dot { border-radius: 50%; background: var(--brand); flex: none; }
  .card--front .brand { left: 30px; top: 60px; font-size: 30px; width: 260px; }
  .card--front .brand__dot { width: 34px; height: 34px; }
  .card--back .brand { left: 44px; top: 46px; font-size: 24px; width: 220px; }
  .card--back .brand__dot { width: 28px; height: 28px; }

  .wave { position: absolute; height: 8px; z-index: 1; }

  .opening {
    position: absolute; left: 32px; top: 186px;
    color: var(--red); font-size: 27px; font-weight: 500; line-height: 1.12;
    z-index: 2;
  }
  .card--front .wave { left: 0; top: 268px; width: 691px; }

  .hours { position: absolute; left: 32px; top: 304px; color: var(--blue); z-index: 2; }
  .hours__title { font-size: 26px; font-weight: 500; margin-bottom: 4px; }
  .hours__label { font-size: 20px; font-weight: 600; line-height: 1.05; }
  .hours__time { font-size: 20px; font-weight: 400; line-height: 1.05; margin-bottom: 6px; }

  .call-band {
    position: absolute; left: 0; top: 451px; width: 691px; height: 83px; z-index: 1;
  }
  .call {
    position: absolute; left: 32px; top: 474px;
    color: #fff; font-size: 27px; font-weight: 600; z-index: 2;
  }

  .photo { position: absolute; }
  .photo--nurse {
    left: 300px; top: 34px; width: 391px; height: 500px;
    background: radial-gradient(ellipse at 45% 55%, #f6d9c6 0%, #f1cdb6 35%, #e9eef2 65%, #ffffff 100%);
    border-radius: 180px 0 0 0;
  }
  .photo--toddler {
    left: 218px; top: 200px; width: 106px; height: 215px;
    background: radial-gradient(ellipse at 55% 45%, #f08a3a 0%, #f4b58e 40%, #7cc6e4 70%, rgba(255,255,255,0) 100%);
  }

  .stamp {
    position: absolute; left: 571px; top: 24px; width: 88px; height: 100px;
    border: 1px solid var(--ink);
  }
  .divider {
    position: absolute; left: 327px; top: 129px; width: 1px; height: 356px;
    background: var(--ink);
  }
  .address-line {
    position: absolute; left: 362px; width: 290px; height: 1px; background: var(--ink);
  }

  .services { position: absolute; left: 40px; top: 143px; }
  .services__title { color: var(--red); font-size: 22px; font-weight: 500; line-height: 1; }
  .card--back .wave { left: 40px; top: 168px; width: 222px; }
  .services__list {
    position: absolute; left: 40px; top: 180px;
    list-style: none; color: var(--blue);
    font-size: 12px; font-weight: 600; line-height: 14.2px;
  }
  .services__list li::before { content: "• "; }

  .website {
    position: absolute; left: 0; width: 685px; top: 508px;
    text-align: center; color: var(--red); font-size: 20px; font-weight: 500;
  }
</style>
</head>
<body>
  <svg width="0" height="0" style="position:absolute">
    <defs>
      <pattern id="wave-rule" width="10" height="8" patternUnits="userSpaceOnUse">
        <path d="M0 4 Q2.5 1 5 4 T10 4" fill="none" stroke="#f0212c" stroke-width="1"/>
      </pattern>
    </defs>
  </svg>

  <section class="card card--front">
    <div class="photo photo--nurse" role="img" aria-label="Photo of a smiling nurse examining a baby with a stethoscope"></div>
    <svg class="wave" viewBox="0 0 691 8" preserveAspectRatio="none"><rect width="691" height="8" fill="url(#wave-rule)"/></svg>
    <svg class="call-band" viewBox="0 0 691 83">
      <polygon points="0,0 300,0 320,70 340,83 0,83" fill="#f0212c"/>
      <polygon points="628,0 691,0 691,40 640,40" fill="#f0212c"/>
    </svg>

    <div class="brand"><span class="brand__dot"></span><span>Tiny Oak Pediatrics</span></div>

    <h1 class="opening">Urgent Care Opening<br>September 1, 2014</h1>

    <div class="hours">
      <h2 class="hours__title">Hours of operation</h2>
      <p class="hours__label">weekdays</p>
      <p class="hours__time">5pm-9pm</p>
      <p class="hours__label">weekends and holidays</p>
      <p class="hours__time">9am-5pm</p>
    </div>

    <p class="call">Call: (405)628-3194</p>
  </section>

  <section class="card card--back">
    <div class="brand"><span class="brand__dot"></span><span>Tiny Oak Pediatrics</span></div>
    <div class="stamp"></div>
    <div class="divider"></div>
    <div class="address-line" style="top:345px"></div>
    <div class="address-line" style="top:372px"></div>
    <div class="address-line" style="top:400px"></div>
    <div class="address-line" style="top:428px"></div>

    <div class="photo photo--toddler" role="img" aria-label="Photo of a toddler in an orange shirt sitting and holding a toy"></div>

    <h2 class="services"><span class="services__title">Our Services</span></h2>
    <svg class="wave" viewBox="0 0 222 8" preserveAspectRatio="none"><rect width="222" height="8" fill="url(#wave-rule)"/></svg>
    <ul class="services__list">
      <li>Allergies</li>
      <li>Colds and Flu</li>
      <li>Fever</li>
      <li>Flu Shots and Immunizations</li>
      <li>Ear Infections</li>
      <li>Fractures</li>
      <li>Lacerations or Cut Repair</li>
      <li>Stomach Aches</li>
      <li>Sprains and Strains</li>
      <li>Sore Throats</li>
      <li>Vomiting and Diarrhea</li>
      <li>Asthma Attacks (Minor)</li>
      <li>Eye Injury (Minor)</li>
      <li>Migraine</li>
      <li>Injuries</li>
      <li>Wellness Exams</li>
      <li>Pregnancy Testing</li>
      <li>Physicals</li>
      <li>Skin Rashes</li>
      <li>Urinary and Gynecological Infections</li>
      <li>Wart and Skin Tag Removal</li>
    </ul>

    <p class="website">www.tinyoakclinic.com</p>
  </section>
</body>
</html>
```